Flyer für Kunstobjekte im Bereich Tennis und Golf  - formWERK-
Flyer für Kunstobjekte im Bereich Tennis und Golf - formWERK-
Vielen Dank. Es ist alles perfekt gelaufen. Sehr gute Designs. Alle Änderungswünsche wurden schnell bearbeitet. Ich in sehr zufrieden!!!
Zielgruppe
Ich fertige Kunstobjekte im Bereich Tennis und Golf. Die Zielgruppe sind zum einen Tennis- sowie Golfclubs, Organisationen die entsprechende Turniere veranstalten, als auch Magazine und Zeitschriften in dem Bereich.
Ich würde gerne meinen Bekanntheitsgrad steigern und meine Bilder nach außen hin kommunizieren.
Aufgabenstellung
Ich würde gerne ein Flyer gestalten lassen, auf dem meine Bilder gut repräsentiert werden. Auf dem Flyer sollen einige meiner Bilder sein. ( Bevorzugt Wolke, Mut, Blue Oak, 7 Dusk, Kreidel, Lichtfäden, Rim Quest, Faltkern, Sonnenwirbel, Horizon, Moon at dusk) Die Größe der Bilder, sowie die Preise sollen nicht auf dem Flyer sein.

```html
<!DOCTYPE html>
<html lang="de">
<head>
<meta charset="utf-8">
<title>formWERK – Flyer</title>
<link rel="stylesheet" href="https://fonts.googleapis.com/css2?family=Arimo:wght@400;700&display=swap">
<style>
  :root {
    --stage: #f2f2f2;
    --ink-dark: #2b2b2b;
    --panel-grey: #7b7b7b;
    --inner-grey: #5c5c5c;
    --band-black: #141414;
    --teal: #0f9a80;
    --teal-light: #17a88c;
    --white: #ffffff;
    --text-light: #f0f0f0;
    --frame-edge: #d4d4d4;
    --art-green-a: #a9d45a;
    --art-green-b: #7fae3c;
    --art-grey-a: #ececec;
    --art-grey-b: #cfcfcf;
    --art-rust-a: #a8481f;
    --art-rust-b: #8a3514;
    --art-red-a: #c94a43;
    --art-red-b: #b8403a;
  }
  * { box-sizing: border-box; margin: 0; padding: 0; }
  html, body { width: 1200px; height: 981px; overflow: hidden; }
  body {
    background: var(--stage);
    font-family: "Arimo", Arial, sans-serif;
    position: relative;
  }
  .flyer {
    position: absolute;
    left: 140px; top: 65px;
    width: 920px; height: 850px;
    display: flex;
    box-shadow: 0 10px 30px rgba(0,0,0,.18);
  }

  /* Cover panel */
  .cover {
    width: 400px; height: 100%;
    background: var(--panel-grey);
    position: relative;
    color: var(--text-light);
  }
  .cover__head {
    height: 100px;
    background: var(--ink-dark);
    padding: 30px 0 0 30px;
  }
  .cover__name {
    font-weight: 700;
    font-size: 34px;
    color: var(--teal);
    letter-spacing: .5px;
    display: inline-block;
    padding-bottom: 4px;
    border-bottom: 4px solid var(--teal);
  }
  .cover__band {
    margin-top: 110px;
    height: 110px;
    background: var(--teal-light);
    padding: 24px 0 0 30px;
  }
  .cover__title {
    font-size: 56px;
    font-weight: 700;
    color: var(--white);
    letter-spacing: 1px;
  }
  .cover__body { padding: 32px 30px 0 30px; }
  .cover__lead {
    font-size: 22px;
    font-weight: 700;
    margin-bottom: 18px;
  }
  .cover__text {
    font-size: 12.5px;
    line-height: 1.5;
    margin-bottom: 14px;
  }
  .artist {
    position: absolute;
    left: 30px; bottom: 36px; right: 20px;
    display: flex;
    align-items: flex-end;
    gap: 18px;
  }
  .artist__photo {
    width: 140px; height: 170px;
    background: linear-gradient(160deg, #d9d9d9, #8e8e8e);
  }
  .artist__info { font-size: 13px; line-height: 1.45; font-weight: 700; padding-bottom: 6px; }
  .artist__info strong { font-size: 15px; display: block; margin-bottom: 2px; }

  /* Inner panel */
  .gallery {
    width: 520px; height: 100%;
    background: var(--inner-grey);
    position: relative;
  }
  .gallery__band {
    height: 70px;
    background: var(--band-black);
    color: var(--white);
    font-size: 14px;
    font-weight: 700;
    line-height: 1.4;
    padding: 16px 30px 0 30px;
  }
  .frame {
    position: absolute;
    background: var(--white);
    border: 2px solid var(--frame-edge);
    box-shadow: 0 3px 8px rgba(0,0,0,.35);
    display: flex;
    align-items: center;
    justify-content: center;
  }
  .frame__art { box-shadow: inset 0 0 0 2px #e3e3e3; }
  .frame--tall-a { left: 30px; top: 100px; width: 220px; height: 330px; }
  .frame--tall-b { left: 30px; top: 460px; width: 220px; height: 330px; }
  .frame--wide   { left: 280px; top: 100px; width: 210px; height: 190px; }
  .frame--mid    { left: 295px; top: 320px; width: 180px; height: 180px; }
  .frame--stop   { left: 285px; top: 530px; width: 200px; height: 260px; }

  .art-figure    { width: 150px; height: 260px; background: linear-gradient(180deg, var(--art-green-a), var(--art-green-b)); }
  .art-web       { width: 170px; height: 250px; background: linear-gradient(180deg, var(--art-grey-a), var(--art-grey-b)); }
  .art-ball      { width: 120px; height: 100px; background: linear-gradient(180deg, var(--art-grey-a), var(--art-grey-b)); }
  .art-butterfly { width: 120px; height: 110px; background: linear-gradient(180deg, var(--art-rust-a), var(--art-rust-b)); }
  .art-stop      { width: 110px; height: 110px; background: linear-gradient(180deg, var(--art-red-a), var(--art-red-b)); }
</style>
</head>
<body>
  <main class="flyer">
    <section class="cover">
      <header class="cover__head">
        <span class="cover__name">Marlene Hofer</span>
      </header>
      <div class="cover__band">
        <h1 class="cover__title">formWERK</h1>
      </div>
      <div class="cover__body">
        <h2 class="cover__lead">Anlässen Rahmen geben …</h2>
        <p class="cover__text">In meinen Bildern finden Sie golf- und tennisspezifische Wortspiele in kleinen Schaukästen dreidimensional abgebildet. Dem Betrachter bieten sie visuelle Überraschungen und erzählen kleine Geschichten rund um Driver, Greenfee, Breaks und Co. …</p>
        <p class="cover__text">Darüber hinaus entwerfe ich auch Objekte z. B. für Preisverleihungen, Golf-/Tennisturniere; eben für die besonderen Anlässe im Leben. So hat sich schon einige Male der „Moon at dusk – Golfball“ neu inszeniert in einem Objektkasten wieder gefunden.</p>
      </div>
      <div class="artist">
        <div class="artist__photo" role="img" aria-label="Schwarzweißes Porträtfoto der Künstlerin"></div>
        <p class="artist__info"><strong>Marlene Hofer</strong>geb. 1965<br>seit 1999 künstlerisch tätig<br>im Bereich Objektkunst</p>
      </div>
    </section>

    <section class="gallery">
      <div class="gallery__band">Sie suchen ein ungewöhnliches Geschenk<br>für Ihre Spieler?<br>Dann schauen Sie mal hier....</div>
      <div class="frame frame--tall-a"><div class="frame__art art-figure" role="img" aria-label="Foto eines Objektkastens in Grüntönen"></div></div>
      <div class="frame frame--tall-b"><div class="frame__art art-web" role="img" aria-label="Foto eines Objektkastens in Grau- und Weißtönen"></div></div>
      <div class="frame frame--wide"><div class="frame__art art-ball" role="img" aria-label="Foto eines Objektkastens auf hellem Grund"></div></div>
      <div class="frame frame--mid"><div class="frame__art art-butterfly" role="img" aria-label="Foto eines Objektkastens auf rotbraunem Grund"></div></div>
      <div class="frame frame--stop"><div class="frame__art art-stop" role="img" aria-label="Foto eines Objektkastens in Rottönen"></div></div>
    </section>
  </main>
</body>
</html>
```